New business card design needed for Trucking/Staffing company!

I am looking for a business card design. The business name is Harbor Lane Freightworks, LLC. This company is a staffing company for commercial drivers/truck drivers. Most of our customers are trucking/supply companies. Our colors are blue/black/white/grey. The info I have on my current business cards is
-Spot for a name
-2 lines for an address
-3 lines for Office, cell, and fax
-email
-website(currently on backside of card with logo but can go anywhere)
Updates

Project Deadline Extended
Reason: Open to more designs

Target Market(s)

Trucking companies, building supply companies

Industry/Entity Type

Business

Contact Information for Business Card

Edgy but professional

Font styles to use
Other font styles liked:
• Open to suggestions

Colors
0555a3
000000
ffffff
9d9d9d

Requirements
Must have
• Must have the logo incorporated

```html
<!DOCTYPE html>
<html lang="en">
<head>
<meta charset="utf-8">
<title>Harbor Lane Freightworks — Business Card</title>
<link href="https://fonts.googleapis.com/css2?family=Montserrat:wght@700;800&family=Open+Sans:wght@400;700&display=swap" rel="stylesheet">
<style>
  :root {
    --brand-blue: #0555a3;
    --band-blue: #3a5fc8;
    --band-blue-light: #5b7fe0;
    --ink: #000000;
    --paper: #ffffff;
    --steel: #9d9d9d;
    --slate: #4a4c50;
    --slate-dark: #2b2c2f;
    --text-grey: #555a60;
    --backdrop: #e7e6e3;
  }
  * { margin: 0; padding: 0; box-sizing: border-box; }
  html, body { width: 1200px; height: 1023px; overflow: hidden; }
  body {
    background: var(--backdrop);
    font-family: "Open Sans", Arial, sans-serif;
    position: relative;
  }
  .card {
    position: absolute;
    width: 560px;
    height: 320px;
    border-radius: 4px;
    box-shadow: 0 10px 24px rgba(0,0,0,.22);
    overflow: hidden;
  }
  /* Front */
  .card-front { left: 70px; top: 110px; background: var(--paper); }
  .front-art { position: absolute; inset: 0; }
  .front-brand {
    position: absolute; right: 34px; top: 38px;
    font-family: "Montserrat", Arial, sans-serif; font-weight: 700;
    font-size: 15px; letter-spacing: 1px; color: var(--steel);
    text-transform: uppercase; text-align: right; line-height: 1.4;
  }
  .holder { position: absolute; left: 34px; top: 128px; color: var(--paper); }
  .holder-name {
    font-family: "Montserrat", Arial, sans-serif; font-weight: 800;
    font-size: 24px; letter-spacing: 1.5px; text-transform: uppercase; line-height: 1;
  }
  .holder-title { font-size: 12px; font-weight: 700; letter-spacing: 1px; text-transform: uppercase; margin-top: 6px; }
  .contacts { position: absolute; left: 40px; top: 200px; list-style: none; }
  .contacts li {
    display: flex; align-items: center; gap: 8px;
    font-size: 12px; color: var(--text-grey); line-height: 18px;
  }
  .contacts svg { width: 12px; height: 12px; flex: none; }
  .address {
    position: absolute; left: 180px; top: 210px;
    color: var(--band-blue); font-weight: 700; font-size: 12px;
    text-transform: uppercase; line-height: 18px; letter-spacing: .3px;
  }
  /* Back */
  .card-back {
    left: 570px; top: 590px;
    background: linear-gradient(135deg, var(--slate-dark) 0%, var(--slate) 55%, var(--slate-dark) 100%);
  }
  .back-brand {
    position: absolute; left: 0; right: 0; top: 50%; transform: translateY(-50%);
    text-align: center; color: var(--paper);
    font-family: "Montserrat", Arial, sans-serif; font-weight: 800;
    font-size: 30px; letter-spacing: 2px; text-transform: uppercase; line-height: 1.25;
  }
  .back-brand small { display: block; font-size: 30px; }
</style>
</head>
<body>
  <section class="card card-front" aria-label="Business card front">
    <svg class="front-art" viewBox="0 0 560 320" aria-hidden="true">
      <defs>
        <linearGradient id="bandFill" x1="0" y1="0" x2="1" y2="1">
          <stop offset="0" stop-color="#5b7fe0"/>
          <stop offset="1" stop-color="#3a5fc8"/>
        </linearGradient>
      </defs>
      <g stroke="#9d9d9d" stroke-width="2" fill="none">
        <line x1="0" y1="98" x2="360" y2="98"/>
        <line x1="0" y1="106" x2="345" y2="106"/>
        <line x1="0" y1="114" x2="330" y2="114"/>
      </g>
      <polygon points="0,120 330,120 290,186 0,186" fill="url(#bandFill)"/>
      <line x1="0" y1="192" x2="286" y2="192" stroke="#9d9d9d" stroke-width="2"/>
    </svg>
    <div class="front-brand">Harbor Lane<br>Freightworks</div>
    <div class="holder">
      <p class="holder-name">Dana Whitfield</p>
      <p class="holder-title">Director</p>
    </div>
    <ul class="contacts">
      <li><svg viewBox="0 0 12 12"><circle cx="6" cy="6" r="6" fill="#9d9d9d"/><path d="M4 3.2l1 1.6-.6.7c.4.9 1.1 1.6 2 2l.7-.6 1.6 1-.5 1.1C6 8.8 3.2 6 3 3.7z" fill="#fff"/></svg>555-014-2290</li>
      <li><svg viewBox="0 0 12 12"><circle cx="6" cy="6" r="6" fill="#9d9d9d"/><rect x="4" y="2.5" width="4" height="7" rx=".8" fill="#fff"/></svg>555-018-7310</li>
      <li><svg viewBox="0 0 12 12"><circle cx="6" cy="6" r="6" fill="#9d9d9d"/><rect x="3" y="4" width="6" height="4.2" fill="#fff"/><path d="M3 4l3 2.4L9 4" stroke="#9d9d9d" stroke-width=".8" fill="none"/></svg>dana@harborlanefreight.com</li>
      <li><svg viewBox="0 0 12 12"><circle cx="6" cy="6" r="6" fill="#9d9d9d"/><circle cx="6" cy="6" r="3.3" stroke="#fff" stroke-width=".8" fill="none"/><path d="M2.7 6h6.6M6 2.7v6.6" stroke="#fff" stroke-width=".8"/></svg>www.harborlanefreight.com</li>
    </ul>
    <p class="address" style="top:278px;left:40px;">418 Quayside Road Building<br>9th Floor Quayside Rd. Eastport, Marlow 20417</p>
  </section>

  <section class="card card-back" aria-label="Business card back">
    <p class="back-brand">Harbor Lane<small>Freightworks</small></p>
  </section>
</body>
</html>
```